依頼概要
■ 依頼の目的/概要

移動販売車の脇に設置するのぼりになります。

■ デザインへの要望

地元の主要農産物(米)をつかっていることを強くアピールし、地域活性につながるような商品(特産品)にしたいです。
商品名は、『ユメサラクレープ』・・・「ユメサラ」とは、岐阜地方で主に栽培されいてる米の銘柄で、実際美味しいです。
県外での『ユメサラ』の認知度を上げることと『ユメサラの生産者』に知ってもらうことが目的なので、メインワードを強調したシンプルなデザインを希望します。
現段階でのイメージは、筆書体かなと思っています。

添付①のテンプレートを使用して、作成してください。(当方、イラストレーター未所持ですので、実際開けるのか確認できません。開けない場合は、お手数ですが、下記のサイトから、ダウンロードをお願いいたします。)
http://www.kasuriya-web.com/original/download.php

また、添付②のロゴマークも組み込んでください。

■店の情報
ユメサラの米粉クレープとタピオカドリンクを可愛いロデルバスで販売しています。
販売場所は、サービスエリア、イベント会場、店舗の駐車場などです。
メイン客層は、女子高校生・大学生などですが、『ユメサラの生産者』である年配の方々にも興味をもっていただきたいです。

参考資料として、実際の車両の画像(添付③)を載せます。あわせて、ご確認下さい。

★キーワード★
メイン(必須) ユメサラクレープ
サブ(必須)  岐阜(県)〔ぎふ(けん)〕
輪之内(町)〔わのうち(ちょう)〕
ロゴマーク

※キーワードの地名は、漢字でも、ひらがなでも構いません。以前は、『岐阜わのうち』で自作したものを使用していました。

■輪之内町の情報
輪之内町は、岐阜県のこの辺りです。添付④確認

■ のぼりの情報

サイズ:横600×縦1800

■ 納品ファイルの希望

イラストレーター形式

■ 進め方

弊社の希望するイメージに近い提案を1つ(場合によって複数)選択させて頂きます。希望に近づけるために、修正要望を個別にさせて頂くこともあります。コンペ方式のため、修正後に当選されない場合も、どうかご了承ください。

■ その他/注意点

選択させて頂いたデザインの著作権(財産権)等の扱いはBrivora利用規約に従い、弊社に譲渡をお願いします。フォントや画像素材などを利用する場合は上記利用用途に使用できることを確認し、第三者の知的財産権等に注意して下さい。
皆様、たくさんの提案ありがとうございます。
すべてと言っていいほどの提案が、イメージ通りの素晴らしい提案です。
ありがとうございます。

今後の修正依頼は、選定後にさせて頂きたく思います。

まだまだ、いろいろな筆文字やデザインを拝見したいと思っております。
引き続きご提案のほど、お願いいたします。

なお、選定は役場(役所)の人や、友人からもっとも支持があったものを選びたいと思います。
残りわずかではございますが、最後までよろしくお願いいたします。
■ 選んだ理由

もっとも支持を集めた提案に決めさせていただきました。
個人的にも、かわいらしさ、バランスの良さが気に入りました。

■ 提案者全員のお礼・コメント

たくさんの提案をしていただき、本当にありがとうございました。
今後ともよろしくお願いいたします。

```html
<!DOCTYPE html>
<html lang="ja">
<head>
<meta charset="utf-8">
<title>ユメサラクレープ のぼり</title>
<link href="https://fonts.googleapis.com/css2?family=Yuji+Boku&family=Yusei+Magic&display=swap" rel="stylesheet">
<style>
  :root {
    --paper: #ffffff;
    --banner-red: #ee2a17;
    --ink: #151515;
    --cream: #fffdf3;
    --gold: #f3c229;
    --shade: #b9871a;
    --leaf: #3f7a2c;
    --brown: #7a4a22;
    --guide: #8a8a8a;
  }
  html, body {
    margin: 0;
    padding: 0;
    width: 1200px;
    height: 2840px;
    overflow: hidden;
    background: var(--paper);
  }
  .canvas {
    position: relative;
    width: 1200px;
    height: 2840px;
    background: var(--paper);
  }
  .spec-label {
    position: absolute;
    left: 180px;
    top: 20px;
    font-family: "Yusei Magic", sans-serif;
    font-size: 22px;
    color: var(--guide);
  }
  .flag {
    position: absolute;
    left: 180px;
    top: 80px;
    width: 900px;
    height: 2680px;
    border: 2px solid #bdbdbd;
    box-sizing: border-box;
    overflow: hidden;
  }
  .flag-head {
    position: absolute;
    left: 0;
    top: 0;
    width: 100%;
    height: 600px;
    background: var(--paper);
    display: flex;
    flex-direction: column;
    align-items: center;
    justify-content: center;
    gap: 24px;
  }
  .brand-name {
    display: flex;
    align-items: center;
    gap: 26px;
    font-family: "Yusei Magic", sans-serif;
    font-size: 130px;
    color: var(--brown);
    line-height: 1;
  }
  .brand-dot {
    width: 70px;
    height: 70px;
    border-radius: 50%;
    background: var(--leaf);
  }
  .brand-sub {
    font-family: "Yusei Magic", sans-serif;
    font-size: 44px;
    color: var(--brown);
    letter-spacing: 6px;
  }
  .flag-body {
    position: absolute;
    left: 0;
    top: 600px;
    width: 100%;
    height: 2080px;
    background: var(--banner-red);
  }
  .place-badge {
    position: absolute;
    left: 190px;
    top: 90px;
    width: 180px;
    height: 780px;
    background: var(--ink);
    transform: rotate(-3deg);
    display: flex;
    flex-direction: column;
    align-items: center;
    justify-content: center;
    clip-path: polygon(0 2%, 10% 0, 100% 1%, 92% 50%, 100% 99%, 8% 100%, 0 97%, 9% 50%);
  }
  .place-name {
    display: flex;
    flex-direction: column;
    align-items: center;
    font-family: "Yusei Magic", sans-serif;
    font-size: 118px;
    color: var(--cream);
    line-height: 1.03;
  }
  .title-column {
    position: absolute;
    display: flex;
    flex-direction: column;
    align-items: center;
    font-family: "Yuji Boku", serif;
    color: var(--cream);
    line-height: 1;
    text-shadow: 8px 8px 0 var(--gold), 12px 12px 0 var(--shade);
    z-index: 2;
  }
  .title-column span { display: block; }
  .product-name {
    left: 560px;
    top: 40px;
    width: 250px;
    font-size: 230px;
  }
  .product-kind {
    left: 240px;
    top: 1000px;
    width: 290px;
    font-size: 260px;
    line-height: 0.96;
  }
  .product-kind .bar { transform: scaleY(1.15); }
  .rice-flour {
    position: absolute;
    left: 590px;
    top: 1020px;
    display: flex;
    flex-direction: column;
    align-items: center;
    font-family: "Yuji Boku", serif;
    font-size: 160px;
    color: var(--ink);
    line-height: 1.05;
    text-shadow: 4px 4px 0 var(--gold);
    z-index: 2;
  }
  .rice-art {
    position: absolute;
    right: 30px;
    bottom: 0;
    width: 320px;
    height: 480px;
    background: linear-gradient(160deg, rgba(243,194,41,0.15), rgba(243,194,41,0.75));
    z-index: 1;
  }
  .tab { position: absolute; }
</style>
</head>
<body>
<div class="canvas">
  <div class="spec-label">のぼり 600×1800</div>

  <svg class="tab" style="left:130px;top:40px" width="80" height="80" viewBox="0 0 80 80" aria-hidden="true">
    <rect x="10" y="10" width="60" height="60" fill="#fff" stroke="#999" stroke-width="3"/>
    <path d="M10 10 L70 70 M70 10 L10 70" stroke="#999" stroke-width="2"/>
  </svg>
  <svg class="tab" style="left:300px;top:40px" width="80" height="80" viewBox="0 0 80 80" aria-hidden="true">
    <rect x="10" y="10" width="60" height="60" fill="#fff" stroke="#999" stroke-width="3"/>
    <path d="M10 10 L70 70 M70 10 L10 70" stroke="#999" stroke-width="2"/>
  </svg>
  <svg class="tab" style="left:130px;top:800px" width="100" height="60" viewBox="0 0 100 60" aria-hidden="true">
    <rect x="6" y="10" width="88" height="40" fill="#fff" stroke="#999" stroke-width="3"/>
  </svg>
  <svg class="tab" style="left:130px;top:1440px" width="100" height="60" viewBox="0 0 100 60" aria-hidden="true">
    <rect x="6" y="10" width="88" height="40" fill="#fff" stroke="#999" stroke-width="3"/>
  </svg>
  <svg class="tab" style="left:130px;top:2070px" width="100" height="60" viewBox="0 0 100 60" aria-hidden="true">
    <rect x="6" y="10" width="88" height="40" fill="#fff" stroke="#999" stroke-width="3"/>
  </svg>
  <svg class="tab" style="left:130px;top:2700px" width="100" height="60" viewBox="0 0 100 60" aria-hidden="true">
    <rect x="6" y="10" width="88" height="40" fill="#fff" stroke="#999" stroke-width="3"/>
  </svg>

  <div class="flag">
    <header class="flag-head">
      <div class="brand-name"><span class="brand-dot"></span>Mirea</div>
      <div class="brand-sub">crepe ・ ミレア ・ tapioca</div>
    </header>

    <section class="flag-body">
      <div class="place-badge">
        <div class="place-name"><span>岐</span><span>阜</span><span>輪</span><span>之</span><span>内</span><span>町</span></div>
      </div>
      <div class="title-column product-name" aria-label="ユメサラ">
        <span>ユ</span><span>メ</span><span>サ</span><span>ラ</span>
      </div>
      <div class="rice-flour" aria-label="米粉"><span>米</span><span>粉</span></div>
      <div class="rice-art" role="img" aria-label="黄金色の稲穂のイラスト"></div>
      <div class="title-column product-kind" aria-label="クレープ">
        <span>ク</span><span>レ</span><span class="bar">｜</span><span>プ</span>
      </div>
    </section>
  </div>
</div>
</body>
</html>
```